依頼詳細
今回はMOZUアプリの広告を利用し、そちらから会員登録が出来る様にする為に、その広告バナーに表示される画像の作成をお願いします。
画像サイズが2種類のデザイン3種類作成お願いします。
記載項目
碧浜ワーク・ネット
サイズ
• 1080×1080px RPG 1200×628px RPG  の2種類
希望イメージ
シンプル 複雑
単色 カラフル
暗い 明るい
日常 高級
遊び心 厳粛
未来的 伝統的
女性的 男性的
希望する色
緑系、青系、無彩色系
納品ファイル
• 高解像度JPG (.jpg)
• イラストレーター形式 (.ai)
• フォトショップ形式 (.psd)
• PNG形式 (.png)
補足説明
参考資料として3つの画像を添付しておりますのでご参考にお願いします。
パターン1が、沖縄県で介護のお仕事をお探しならという内容に変更し、デザインを作成お願い致します。
※給与 月給18万以上・賞与年2回/無資格・未経験者・主婦歓迎!/日曜・その他休み

パターン2はフリーのおもしろ画像を利用して頂き、こんな俺でもなれたよ的な感じでお願いします。
※マネージャー(ケアマネージャー)

パターン3は転職時間をカットの文言を入れて頂き、デザインを作成お願い致します。
※参考パターン1~3の画像サイズ2種類ずつ作成となりますので、合計6の製作依頼となります。

```html
<!DOCTYPE html>
<html lang="ja">
<head>
<meta charset="utf-8">
<title>碧浜ワーク・ネット 転職時間をサクッとカット バナー</title>
<link href="https://fonts.googleapis.com/css2?family=M+PLUS+1p:wght@500;700;900&display=swap" rel="stylesheet">
<style>
  :root {
    --sheet-bg: #d9d9d9;
    --label-bg: #8f8f8f;
    --label-text: #ffffff;
    --banner-yellow: #f3c31c;
    --ink: #1c1a17;
    --kiwi-green: #6fae2a;
    --kiwi-deep: #3f7d1c;
    --bar-white: #ffffff;
    --brand-green: #2f9a4a;
    --cta-red: #c8174a;
  }
  * { margin: 0; padding: 0; box-sizing: border-box; }
  html, body { width: 692px; height: 1200px; overflow: hidden; }
  body {
    background: var(--sheet-bg);
    font-family: "M PLUS 1p", sans-serif;
    color: var(--ink);
    position: relative;
  }
  .banner {
    position: absolute;
    left: 0;
    width: 692px;
    background: var(--banner-yellow);
    overflow: hidden;
  }
  .banner--square { top: 0; height: 692px; }
  .banner--wide { top: 734px; height: 362px; }

  .size-label {
    position: absolute;
    left: 0;
    width: 692px;
    height: 34px;
    background: var(--label-bg);
    color: var(--label-text);
    font-size: 17px;
    font-weight: 500;
    line-height: 34px;
    padding-left: 10px;
  }
  .size-label--square { top: 694px; }
  .size-label--wide { top: 1098px; }

  .kiwi-photo {
    position: absolute;
    background:
      radial-gradient(ellipse at 50% 50%, var(--kiwi-green) 0%, var(--kiwi-deep) 45%, rgba(138,90,43,0.5) 62%, rgba(243,195,28,0) 72%);
  }
  .banner--square .kiwi-photo { left: 50px; top: 40px; width: 600px; height: 290px; }
  .banner--wide .kiwi-photo { left: 20px; top: 20px; width: 330px; height: 270px; }

  .headline {
    position: absolute;
    text-align: center;
    font-weight: 900;
    white-space: nowrap;
  }
  .headline__lead { display: block; letter-spacing: 1px; }
  .headline__main {
    display: block;
    transform: skewX(-12deg);
  }
  .banner--square .headline { left: 0; width: 692px; top: 330px; }
  .banner--square .headline__lead { font-size: 54px; line-height: 70px; }
  .banner--square .headline__main { font-size: 76px; line-height: 100px; }
  .banner--wide .headline { left: 318px; width: 364px; top: 32px; }
  .banner--wide .headline__lead { font-size: 44px; line-height: 60px; }
  .banner--wide .headline__main { font-size: 42px; line-height: 70px; }

  .brand-bar {
    position: absolute;
    left: 0;
    bottom: 0;
    width: 100%;
    background: var(--bar-white);
    display: flex;
    align-items: center;
    justify-content: space-between;
    white-space: nowrap;
  }
  .banner--square .brand-bar { height: 96px; padding: 0 18px 0 22px; }
  .banner--wide .brand-bar { height: 48px; padding: 0 36px 0 72px; }

  .brand-name {
    display: flex;
    align-items: center;
    color: var(--brand-green);
    font-weight: 700;
  }
  .brand-name__mark { background: var(--brand-green); margin-right: 8px; }
  .banner--square .brand-name { font-size: 30px; }
  .banner--square .brand-name__mark { width: 26px; height: 26px; }
  .banner--wide .brand-name { font-size: 20px; }
  .banner--wide .brand-name__mark { width: 16px; height: 16px; }

  .cta-button {
    background: var(--cta-red);
    color: #fff;
    font-weight: 700;
    display: flex;
    align-items: center;
    border-radius: 3px;
  }
  .cta-button svg { margin-left: 8px; fill: #fff; }
  .banner--square .cta-button { font-size: 26px; height: 58px; padding: 0 16px 0 22px; }
  .banner--wide .cta-button { font-size: 17px; height: 32px; padding: 0 12px 0 18px; }
</style>
</head>
<body>

  <section class="banner banner--square">
    <div class="kiwi-photo" role="img" aria-label="輪切りのキウイとブルーベリーが宙に舞う写真"></div>
    <h1 class="headline">
      <span class="headline__lead">転職時間を</span>
      <span class="headline__main">サクッとカット!</span>
    </h1>
    <div class="brand-bar">
      <div class="brand-name"><span class="brand-name__mark"></span>碧浜ワーク・ネット</div>
      <div class="cta-button">詳しくはこちら<svg width="12" height="14" viewBox="0 0 12 14"><polygon points="0,0 12,7 0,14"/></svg></div>
    </div>
  </section>
  <div class="size-label size-label--square">1080 x 1080_03</div>

  <section class="banner banner--wide">
    <div class="kiwi-photo" role="img" aria-label="輪切りのキウイとブルーベリーが宙に舞う写真"></div>
    <h2 class="headline">
      <span class="headline__lead">転職時間を</span>
      <span class="headline__main">サクッとカット!</span>
    </h2>
    <div class="brand-bar">
      <div class="brand-name"><span class="brand-name__mark"></span>碧浜ワーク・ネット</div>
      <div class="cta-button">詳しくはこちら<svg width="9" height="10" viewBox="0 0 12 14"><polygon points="0,0 12,7 0,14"/></svg></div>
    </div>
  </section>
  <div class="size-label size-label--wide">1200 x 628_03</div>

</body>
</html>
```